Quarrow financial services, is a financial company that provides consultancy, brokerage services, and funding.

we will be providing the clients with insights, knowledge and data with regards to the financial markets.

with the brokerage services we will try to find the suitable counterparts that provide them with the best investments that suits their needs and expected return.

Target Market(s)

financial institutions, Corporates, high-net worth individuals

Industry/Entity Type

Financial Service

Contact Information for Business Card

Font styles to use
Other font styles liked:
• applemyungjo

Colors
00a990
848484

Requirements
Must have
• the logo at the back
Nice to have
• Finesse
Should not have
• boldness

```html
<!DOCTYPE html>
<html lang="en">
<head>
<meta charset="utf-8">
<title>Quarrow Financial Services – Business Card</title>
<link rel="stylesheet" href="https://fonts.googleapis.com/css2?family=Nanum+Myeongjo:wght@400&family=Open+Sans:wght@400&display=swap">
<style>
  :root {
    --backdrop: #e9e7e3;
    --card-black: #050505;
    --card-sheen: #2a2a2a;
    --brand-grey: #8d949b;
    --mark-tile: #dfe4d6;
    --teal: #00c1b0;
    --holder-text: #d6d6d6;
    --ink: #0a0a0a;
  }
  * { margin: 0; padding: 0; box-sizing: border-box; }
  html, body { width: 1200px; height: 902px; overflow: hidden; }
  body {
    background: var(--backdrop);
    position: relative;
    font-family: "Open Sans", Arial, sans-serif;
  }
  .card {
    position: absolute;
    left: 250px;
    width: 700px;
    height: 400px;
    border-radius: 4px;
    overflow: hidden;
    background: linear-gradient(135deg, var(--card-sheen) 0%, var(--card-black) 45%, var(--card-black) 100%);
    box-shadow: 0 10px 28px rgba(0,0,0,0.28);
  }
  .card--front { top: 36px; }
  .card--back  { top: 466px; }

  /* Brand lockup: one font, one weight, one colour, one plain square */
  .brand {
    position: absolute;
    text-align: center;
    font-family: "Nanum Myeongjo", Georgia, serif;
    font-weight: 400;
    color: var(--brand-grey);
  }
  .brand__mark {
    display: block;
    width: 46px; height: 46px;
    margin: 0 auto 18px;
    background: var(--mark-tile);
  }
  .brand__name {
    font-size: 52px;
    letter-spacing: 3px;
    line-height: 1;
  }
  .brand__sub {
    font-size: 13px;
    letter-spacing: 4px;
    text-transform: uppercase;
    margin-top: 8px;
  }
  .card--front .brand { left: 0; right: 0; top: 120px; }

  .card--back .brand { left: 60px; top: 44px; }
  .card--back .brand__mark { width: 40px; height: 40px; margin-bottom: 14px; }
  .card--back .brand__name { font-size: 38px; }
  .card--back .brand__sub { font-size: 10px; letter-spacing: 3px; margin-top: 6px; }

  .card__swoosh { position: absolute; inset: 0; width: 700px; height: 400px; }

  .holder { position: absolute; left: 60px; top: 222px; }
  .holder__name { font-size: 24px; color: var(--holder-text); line-height: 1.15; }
  .holder__role { font-size: 20px; color: var(--teal); line-height: 1.15; }

  .contact { position: absolute; left: 460px; top: 250px; list-style: none; }
  .contact__item {
    display: flex; align-items: center;
    font-size: 19px; color: var(--ink);
    height: 30px;
  }
  .contact__icon { width: 20px; height: 20px; margin-right: 12px; flex: none; }
</style>
</head>
<body>

<section class="card card--front">
  <div class="brand">
    <span class="brand__mark"></span>
    <div class="brand__name">QUARROW</div>
    <div class="brand__sub">Financial Services</div>
  </div>
</section>

<section class="card card--back">
  <svg class="card__swoosh" viewBox="0 0 700 400" aria-hidden="true">
    <defs>
      <linearGradient id="silverBand" x1="0" y1="0" x2="1" y2="1">
        <stop offset="0" stop-color="#d9d9d9"/>
        <stop offset="1" stop-color="#848484"/>
      </linearGradient>
      <linearGradient id="tealField" x1="0" y1="0" x2="1" y2="1">
        <stop offset="0" stop-color="#00c9b6"/>
        <stop offset="1" stop-color="#00a990"/>
      </linearGradient>
    </defs>
    <path d="M430,0 C420,230 230,350 0,400 L700,400 L700,0 Z" fill="url(#silverBand)"/>
    <path d="M500,0 C480,240 300,355 30,400 L700,400 L700,0 Z" fill="#ffffff"/>
    <path d="M504,0 C484,242 306,357 40,400 L700,400 L700,0 Z" fill="url(#tealField)"/>
  </svg>

  <div class="brand">
    <span class="brand__mark"></span>
    <div class="brand__name">QUARROW</div>
    <div class="brand__sub">Financial Services</div>
  </div>

  <div class="holder">
    <div class="holder__name">Daniel Renner</div>
    <div class="holder__role">owner</div>
  </div>

  <ul class="contact">
    <li class="contact__item">
      <svg class="contact__icon" viewBox="0 0 20 20" aria-hidden="true">
        <rect width="20" height="20" rx="4" fill="#0a0a0a"/>
        <path d="M6 5 L8.5 5 L9.5 8 L8 9 C8.8 10.8 9.7 11.7 11 12.3 L12 10.8 L15 11.8 L15 14.3 C10 15 5 10 6 5 Z" fill="#fff"/>
      </svg>
      555-014-2290
    </li>
    <li class="contact__item">
      <svg class="contact__icon" viewBox="0 0 20 20" aria-hidden="true">
        <rect width="20" height="20" rx="4" fill="#0a0a0a"/>
        <rect x="4" y="6" width="12" height="8" fill="none" stroke="#fff" stroke-width="1.4"/>
        <path d="M4 6 L10 11 L16 6" fill="none" stroke="#fff" stroke-width="1.4"/>
      </svg>
      hello@quarrow.com
    </li>
    <li class="contact__item">
      <svg class="contact__icon" viewBox="0 0 20 20" aria-hidden="true">
        <rect width="20" height="20" rx="4" fill="#0a0a0a"/>
        <path d="M10 3.5 C7 3.5 5.5 5.6 5.5 7.8 C5.5 10.8 10 16 10 16 C10 16 14.5 10.8 14.5 7.8 C14.5 5.6 13 3.5 10 3.5 Z" fill="#fff"/>
        <circle cx="10" cy="7.8" r="1.7" fill="#0a0a0a"/>
      </svg>
      480 Linden Grove Rd
    </li>
  </ul>
</section>

</body>
</html>
```